Business Card Design for a Personal Trainer

I need a business card design for my job as a personal trainer. It should have a unique, modern and exclusive design. On the front there should be only my logo with my name and my job. 0163/2918374 Tobias Kellinger Lindenfeldweg 14 80412 Munich Germany The most important contact information is the web adress. it can be bigger than the rest, but its not necessary. The card should be 8,5cmx5,5cm big. Font: Roboto. Colors: black, white, gray, 56c1ff.

```html
<!DOCTYPE html>
<html lang="de">
<head>
<meta charset="utf-8">
<title>Tobias Kellinger – Personal Trainer Visitenkarte</title>
<link rel="stylesheet" href="https://fonts.googleapis.com/css2?family=Roboto:wght@400;700;900&family=Roboto+Condensed:wght@400;500&family=Montserrat:wght@600;700&display=swap">
<style>
  :root {
    --stage: #fb9a06;
    --card: #ffffff;
    --blue: #56c1ff;
    --blue-light: #8ad0fb;
    --ink: #111111;
    --gray: #6f6f6f;
    --photo-dark: #2a2a2a;
    --photo-mid: #8a7a72;
  }
  * { margin: 0; padding: 0; box-sizing: border-box; }
  html, body { width: 1200px; height: 1200px; overflow: hidden; }
  body { background: var(--stage); position: relative; font-family: "Roboto", sans-serif; color: var(--ink); }

  .card { position: absolute; left: 146px; width: 940px; height: 560px; background: var(--card); overflow: hidden; }
  .card--front { top: 32px; }
  .card--back { top: 608px; }
  .card__shapes { position: absolute; inset: 0; width: 100%; height: 100%; }

  /* front */
  .brand { position: absolute; left: 138px; top: 40px; width: 150px; display: flex; flex-direction: column; align-items: center; gap: 8px; }
  .brand__mark { width: 22px; height: 22px; background: var(--ink); }
  .brand__name { font-family: "Roboto", sans-serif; font-weight: 700; font-size: 15px; letter-spacing: 0.2px; color: var(--ink); white-space: nowrap; }

  .showcase { position: absolute; left: 28px; top: 166px; width: 372px; height: 252px; }
  .showcase__frame { position: absolute; inset: 0; width: 100%; height: 100%; }
  .showcase__photo { position: absolute; left: 15px; top: 27px; width: 343px; height: 201px;
    background: linear-gradient(100deg, var(--photo-mid) 0%, var(--photo-dark) 30%, var(--photo-dark) 55%, #b88b80 75%, #6c625e 100%); }

  .identity { position: absolute; left: 500px; top: 234px; width: 420px; text-align: center; }
  .identity__name { font-weight: 900; font-size: 39px; letter-spacing: -0.5px; line-height: 1; white-space: nowrap; }
  .identity__name .accent { color: #ffffff; }
  .identity__role { margin-top: 8px; font-weight: 400; font-size: 26px; line-height: 1; }

  /* back */
  .contacts { position: absolute; left: 21px; top: 163px; list-style: none; }
  .contact { display: flex; align-items: center; position: absolute; left: 0; white-space: nowrap; }
  .contact__icon { width: 58px; height: 58px; border-radius: 50%; background: #ffffff; display: flex; align-items: center; justify-content: center; flex: none; }
  .contact__icon svg { width: 32px; height: 32px; }
  .contact__text { margin-left: 13px; }
  .contact--web { top: 0; }
  .contact--web .contact__text { font-family: "Roboto Condensed", sans-serif; font-weight: 500; font-size: 36px; letter-spacing: -0.8px; }
  .contact--mail { top: 62px; }
  .contact--mail .contact__text { font-family: "Roboto", sans-serif; font-weight: 500; font-size: 32px; }
  .contact--phone { top: 126px; }
  .contact--phone .contact__text { font-family: "Montserrat", sans-serif; font-weight: 700; font-size: 30px; letter-spacing: 1px; }
  .contact--address { top: 188px; }
  .contact--address .contact__text { font-family: "Montserrat", sans-serif; font-weight: 700; font-size: 28px; line-height: 0.95; letter-spacing: 0.5px; }

  .portrait { position: absolute; left: 553px; top: 140px; width: 324px; height: 324px; border-radius: 50%; border: 5px solid var(--blue);
    background: radial-gradient(circle at 50% 45%, #3a3a3a 0%, #1c1c1c 45%, #050505 75%); }
</style>
</head>
<body>

<section class="card card--front">
  <svg class="card__shapes" viewBox="0 0 1174 700" preserveAspectRatio="none" aria-hidden="true">
    <circle cx="1050" cy="340" r="528" fill="var(--blue)"/>
    <circle cx="1160" cy="440" r="550" fill="var(--blue-light)"/>
  </svg>

  <div class="brand">
    <span class="brand__mark"></span>
    <span class="brand__name">TOBIAS KELLINGER</span>
  </div>

  <div class="showcase">
    <div class="showcase__photo" role="img" aria-label="Foto: Personal Trainer im Gespräch mit einer Kundin im Fitnessstudio"></div>
    <svg class="showcase__frame" viewBox="0 0 372 252" aria-hidden="true" fill="none" stroke="#111" stroke-width="5">
      <polyline points="2.5,40 2.5,2.5 46,2.5"/>
      <polyline points="326,2.5 369.5,2.5 369.5,40"/>
      <polyline points="2.5,212 2.5,249.5 46,249.5"/>
      <polyline points="326,249.5 369.5,249.5 369.5,212"/>
    </svg>
  </div>

  <div class="identity">
    <h1 class="identity__name">TOBIAS <span class="accent">KELLINGER</span></h1>
    <p class="identity__role">PERSONAL TRAINER</p>
  </div>
</section>

<section class="card card--back">
  <svg class="card__shapes" viewBox="0 0 1174 700" preserveAspectRatio="none" aria-hidden="true">
    <circle cx="260" cy="350" r="380" fill="var(--blue)"/>
  </svg>

  <ul class="contacts">
    <li class="contact contact--web">
      <span class="contact__icon">
        <svg viewBox="0 0 24 24" fill="none" stroke="#111" stroke-width="1.6"><circle cx="12" cy="12" r="9"/><ellipse cx="12" cy="12" rx="4" ry="9"/><line x1="3" y1="12" x2="21" y2="12"/><path d="M5 7.5h14M5 16.5h14"/></svg>
      </span>
      <span class="contact__text">www.Tobiaskellinger.de</span>
    </li>
    <li class="contact contact--mail">
      <span class="contact__icon">
        <svg viewBox="0 0 24 24" fill="none" stroke="#111" stroke-width="1.6"><rect x="3" y="6" width="18" height="12" rx="1"/><polyline points="3,6 12,13 21,6"/></svg>
      </span>
      <span class="contact__text">t.kellinger@postfach.de</span>
    </li>
    <li class="contact contact--phone">
      <span class="contact__icon">
        <svg viewBox="0 0 24 24" fill="none" stroke="#111" stroke-width="1.6"><rect x="7" y="2.5" width="10" height="19" rx="1.5"/><line x1="11" y1="18.5" x2="13" y2="18.5"/></svg>
      </span>
      <span class="contact__text">0163/2918374</span>
    </li>
    <li class="contact contact--address">
      <span class="contact__icon">
        <svg viewBox="0 0 24 24"><path d="M12 2a7 7 0 0 0-7 7c0 5 7 13 7 13s7-8 7-13a7 7 0 0 0-7-7z" fill="#111"/><circle cx="12" cy="9" r="2.6" fill="#fff"/></svg>
      </span>
      <span class="contact__text">Lindenfeldweg 14<br>80412 Muchen</span>
    </li>
  </ul>

  <div class="portrait" role="img" aria-label="Porträtfoto des Trainers in Schwarzweiß mit verschränkten Armen"></div>
</section>

</body>
</html>
```